Harbourline Panels Brochure

Harbourline Panels New Brochure Brief
Harbourline Panels are manufacturers of kitchen and wardrobe doors. We have 2 target markets, one is business to business and the other business to residential customers.
The main message of our business to residential is to inform them that they can give their kitchen or wardrobe a facelift by just replacing doors and save thousands of dollars by doing this partial renovation. However, this is in direct conflict with our business to business customers (kitchen and wardrobe companies) who buy doors from us and sell complete new kitchens and built in wardrobes to the same residential customers.
Please find links to the Harbourline Panels brochure and website below for your reference. The current dimensions of the brochure is approx. 21cmH x 29.7cmW. https://harbourlinepanels.com.au/harbourlinepanelsbrochure-2/ https://harbourlinepanels.com.au/
I would like to keep the layout of the brochure internal pages consistent with the current design, however, I am open to your ideas. The orange colour as seen on the front page should be a dominant theme as it’s based on our logo however not too overpowering, I prefer to cover to be white. I would like a new front page design, changing the door photos (they will be shades of white, not coloured) and also delete the words ‘ultimate door collection’. Heading to be along the lines of “Custom made kitchen and wardrobe doors”.
On the internal pages, some new door designs will be added and some deleted. s. We are thinking of changing all the door colours to shades of white but also stating that Harbourline Panels can colour match to any major Australian paint brand.
I would like to include a page for Wardrobe Doors with some photos, text and layout options (photo attached). Please add in the before and after images. Please create a before and after using Rob's kitchen in same layout as wardrobe before and after. Please ensure oven is cut from after image. Please add in the photos attached in this brief.
We would also like to include a FAQs section. Some more text describing our product, such as raw material, thickness of doors, painted or unpainted finish and delivery information is to be added.
Re: the ‘edges’ top of page 3; some will be deleted and one new type of edge will be added.
From page 4 onwards, there are different shapes at the bottom of each door design. We are looking for a new way to communicate this as at the moment it is taking up too much room and people do not readily understand that these door patterns can be supplied in the shapes shown in the little diagrams below them.
Please keep in mind all this information will be given at the time of design. I would like to possibly keep the brochure at 8 pages (as it is now). There may be some other changes along the way as this is still in the preliminary stage. Please include the image of our showroom in the brochure mock up.
I look forward to your reply.
Kind Regards,
Greta
* Please note, the images attach with the individual doors need to be changed to some neutral shades such as white, off white, grey, cream etc (similar to the website: https://harbourlinepanels.com.au/kitchen-doors/)

```html
<!DOCTYPE html>
<html lang="en">
<head>
<meta charset="utf-8">
<title>Harbourline Panels – FAQs and Contact</title>
<link rel="stylesheet" href="https://fonts.googleapis.com/css2?family=Titillium+Web:wght@700;900&family=Source+Sans+3:wght@400;700&display=swap">
<style>
  :root {
    --orange: #f7993a;
    --ink: #231f20;
    --paper: #ffffff;
    --photo-light: #f3f1e6;
    --photo-mid: #d9d4c8;
    --photo-dark: #8a3a2c;
  }
  * { margin: 0; padding: 0; box-sizing: border-box; }
  html, body { width: 1200px; height: 848px; overflow: hidden; background: var(--paper); }
  .page {
    position: relative; width: 1200px; height: 848px;
    font-family: "Source Sans 3", "Myriad Pro", sans-serif; color: var(--ink);
  }
  .kitchen-photo {
    position: absolute; left: 1px; top: 0; width: 644px; height: 629px;
    background:
      linear-gradient(180deg, transparent 0 70%, var(--photo-dark) 70% 71.5%, transparent 71.5%),
      linear-gradient(180deg, #f4f3dc 0%, var(--photo-light) 30%, var(--photo-mid) 55%, var(--photo-light) 75%, #ecebe4 100%);
  }
  .bar { position: absolute; background: var(--orange); }
  .heading {
    position: absolute; font-family: "Titillium Web", "Arial Narrow", sans-serif;
    font-weight: 900; color: var(--orange); font-size: 44px; line-height: 1;
    letter-spacing: 0.5px; text-transform: uppercase;
  }
  .hours { position: absolute; left: 38px; top: 708px; font-size: 16px; line-height: 21px; }
  .page-number { position: absolute; left: 27px; top: 783px; font-size: 22px; line-height: 24px; }
  .faq { position: absolute; left: 837px; top: 56px; }
  .faq .eyebrow { font-size: 19px; letter-spacing: 0.5px; line-height: 24px; }
  .faq .heading { position: static; margin-top: 6px; }
  .faq .lead { margin-top: 52px; font-weight: 700; font-size: 16.5px; line-height: 20px; }
  .faq ul { list-style: none; margin-top: 10px; }
  .faq li { font-size: 16.5px; line-height: 30px; padding-left: 16px; position: relative; }
  .faq li::before { content: "-"; position: absolute; left: 3px; }
  .contact { position: absolute; left: 837px; top: 482px; }
  .contact .heading { position: static; }
  .contact address { font-style: normal; margin-top: 17px; }
  .contact p { font-size: 16.5px; line-height: 30px; }
  .contact .email { color: var(--orange); }
</style>
</head>
<body>
<main class="page">
  <div class="kitchen-photo" role="img" aria-label="Photo of a white kitchen with handled cabinets, a range hood and hanging utensils"></div>
  <div class="bar" style="left:1px;top:631px;width:455px;height:9px"></div>
  <div class="bar" style="left:483px;top:631px;width:162px;height:9px"></div>

  <h2 class="heading" style="left:38px;top:668px">Opening Hours</h2>
  <div class="hours">
    <p>Monday to Thursday 8am to 4pm</p>
    <p>Friday 8am to 1pm</p>
  </div>

  <div class="bar" style="left:0;top:780px;width:334px;height:29px"></div>
  <div class="bar" style="left:345px;top:780px;width:305px;height:29px"></div>
  <div class="bar" style="left:661px;top:780px;width:108px;height:29px"></div>
  <span class="page-number">5</span>

  <section class="faq">
    <p class="eyebrow">(GOT A QUESTION?)</p>
    <h2 class="heading">F.A.Qs</h2>
    <p class="lead">* I&nbsp; Want to Know More About:</p>
    <ul>
      <li>Kitchen doors and panels</li>
      <li>Door handles</li>
      <li>Hinges</li>
      <li>Wardrobe doors</li>
      <li>Wardrobe tracks</li>
      <li>Measuring &amp; Installation</li>
    </ul>
  </section>

  <section class="contact">
    <h2 class="heading">Contact Us</h2>
    <address>
      <p>HARBOURLINE PANELS</p>
      <p>Visit our showroom and factory:</p>
      <p>42 Tideway Road</p>
      <p>KELSO BAY NSW 2190</p>
      <p>Phone: (02) 9555 0142</p>
      <p>Fax: (02) 9555 0143</p>
      <p class="email">Email: sales@harbourlinepanels.com.au</p>
    </address>
  </section>
</main>
</body>
</html>
```